Flyer-Design für Zweithaar Studio
Zielgruppe
Firma MOLVA Ketz ist ein Zweithaar Studio. Hier erhalten Kunden individuell auf sie zugeschnittene Perücken und Toupets. Unsere Zielgruppe sind Männer und Frauen mit wenig oder keiner Kopfbehaarung oder Menschen die krankheitsbedingt unter Haarausfall leiden.
Aufgabenstellung
Bitte Vorschläge zu Anzahl Seiten und Format erstellen, aktuell haben wir noch keine Vorstellung dazu. Folgende Inhalte haben wir schon mal als Entwurf vorbereitet:
Eine Seite zum Thema Toupets mit dem Bild vom Mann:
Leiden Sie an übermäßigem Haarausfall?
Fühlen Sie sich nicht mehr 100% wohl damit und möchten gerne wieder Ihre Attraktivität und vor allem das Wohlbefinden steigern?
Dann sind Sie bei uns sehr gut aufgehoben, denn wir können Ihnen Ihr Toupet individuell auf Ihre Bedürfnisse hin z.B. Farbe, Grauanteil, Größe und Styling anpassen.
Eine Seite zum Thema Perücken mit dem Bild der Frau:
Sind Sie an einer Perücke interessiert die augenscheinlich keinen Unterschied zu gewachsenem Haar aufweist?
Dann sind Sie bei uns an der richtigen Adresse. Die langjährige Erfahrung im Zweithaar Bereich von Friseurmeisterin verspricht Ihnen optimale Beratung und ein individuell auf Sie abgestimmtes Produkt.
Bei uns erhalten Sie Zugriff auf verschiedene Modelle im gesamten Preisspektrum.
Liegt eine von Ihrem Arzt attestierte Erkrankung vor, übernimmt Ihre Krankenkasse höchstwahrscheinlich die Kosten für Ihr Zweithaar. Die Formalitäten dazu erledigen wir gerne für Sie um Ihnen unnötigen Stress zu ersparen.
Eine weitere Seite mit den besonderen Merkmalen mit dem Bild Diversity:
Mit unserer Befestigungsmethode sind Sie sehr flexibel - starker halt für jede Situation und auf Wunsch auch abnehmbar z.B. nachts beim schlafen.
Der große Vorteil unserer Befestigungsmethode liegt darin, dass Sie diese selbst umsetzen können und somit nicht jeden Monat das Studio zur Neubefestigung aufsuchen müssen. Das spart Ihnen Zeit und Geld.
Wir können Ihnen Toupets und Perücken in allen Preisklassen anbieten, in verschiedenen Farben, auf Wunsch mit Grauanteil passend zum Alter des Trägers. Unsere Friseurmeisterin Frau Tiltrop berät Sie gerne, natürlich unverbindlich und kostenlos.

```html
<!DOCTYPE html>
<html lang="de">
<head>
<meta charset="utf-8">
<title>MOLVA Ketz – Zweithaar Flyer</title>
<link href="https://fonts.googleapis.com/css2?family=Fira+Sans+Condensed:wght@300;600&display=swap" rel="stylesheet">
<style>
  :root {
    --bg: #e9e9e7;
    --black: #050505;
    --charcoal: #2b2b2b;
    --graphite: #3d3d3d;
    --panel-light: #6b6d6e;
    --panel-dark: #4a4b4c;
    --white: #ffffff;
    --paper: #f7f7f7;
    --ink: #111111;
    --body-grey: #555555;
    --body-light: #d8d8d8;
  }
  * { margin: 0; padding: 0; box-sizing: border-box; }
  html, body { width: 1200px; height: 802px; overflow: hidden; background: var(--bg); }
  body { font-family: "Fira Sans Condensed", sans-serif; }
  .canvas { position: relative; width: 1200px; height: 802px; overflow: hidden; background: var(--bg); }

  .page { position: absolute; overflow: hidden; }
  .photo { position: absolute; }

  .brand {
    position: absolute; display: flex; align-items: center; gap: 6px;
    color: var(--white); font-weight: 600; text-transform: uppercase;
    letter-spacing: 0.06em; white-space: nowrap;
  }
  .brand-mark { width: 7px; height: 7px; background: var(--white); }

  .headline { position: absolute; font-weight: 600; text-transform: uppercase; line-height: 1.6; }
  .copy { position: absolute; font-weight: 300; line-height: 1.65; }

  .divider { position: absolute; display: flex; align-items: center; gap: 5px; }
  .divider-line { width: 22px; height: 1px; background: currentColor; }
  .divider-dot { width: 4px; height: 4px; border: 1px solid currentColor; }

  /* Spread 1: features + cover */
  .features-page { left: 134px; top: 117px; width: 378px; height: 269px; background: var(--paper); }
  .features-band { position: absolute; left: 0; top: 0; width: 100%; height: 118px; background: var(--black); }
  .features-photo { left: 17px; top: 31px; width: 333px; height: 108px;
    background: linear-gradient(90deg, #8a6a55, #c79c86 30%, #b88a70 55%, #d2b5a4 75%, #9a7a66); }
  .features-page .headline { left: 17px; top: 156px; width: 250px; font-size: 7.3px; color: var(--ink); }
  .features-page .copy { top: 201px; width: 150px; font-size: 5.6px; color: var(--body-grey); }
  .copy-left { left: 17px; }
  .copy-right { left: 182px; }

  .cover-page { left: 512px; top: 117px; width: 378px; height: 269px;
    background: linear-gradient(100deg, #1c1c1c 0%, #3a3a3a 55%, #2d2d2d 100%); }
  .cover-photo { left: 224px; top: 0; width: 154px; height: 269px;
    background: radial-gradient(ellipse at 55% 45%, #c59a82 0%, #9b7a6a 35%, #6e5e57 70%, #3a3a3a 100%); }
  .cover-page .brand { left: 52px; top: 40px; font-size: 24px; }

  /* Spread 2: toupet + perücke */
  .toupet-page { left: 134px; top: 416px; width: 378px; height: 268px; background: var(--black); }
  .toupet-photo { left: 175px; top: 0; width: 203px; height: 268px;
    background: linear-gradient(135deg, #3a2a22 0%, #5c4636 35%, #8d6b55 55%, #2e3440 80%, #1b1e24 100%); }
  .toupet-page .headline { left: 16px; top: 57px; width: 150px; font-size: 7.6px; color: var(--white); }
  .toupet-page .headline p + p { margin-top: 8px; }
  .toupet-page .divider { left: 16px; top: 171px; color: var(--white); }
  .toupet-page .copy { left: 16px; top: 181px; width: 138px; font-size: 5.8px; color: var(--body-light); }
  .toupet-page .brand { left: 232px; top: 212px; font-size: 18px; }

  .wig-page { left: 512px; top: 416px; width: 378px; height: 268px; background: var(--charcoal); }
  .wig-photo { left: 243px; top: 0; width: 135px; height: 268px;
    background: radial-gradient(ellipse at 60% 40%, #d6a48b 0%, #a4563f 40%, #6d2a1f 70%, #2a1614 100%); }
  .wig-panel { position: absolute; left: 1px; top: 22px; width: 242px; height: 229px;
    background: linear-gradient(180deg, var(--panel-light), var(--panel-dark)); }
  .wig-panel .headline { left: 24px; top: 35px; width: 220px; font-size: 7.6px; color: var(--white); }
  .wig-panel .divider { left: 24px; top: 93px; color: var(--white); }
  .wig-panel .copy { left: 24px; width: 196px; font-size: 5.8px; color: var(--body-light); }
  .wig-copy-1 { top: 104px; }
  .wig-copy-2 { top: 165px; }

  /* Single card */
  .card { left: 672px; top: 262px; width: 380px; height: 270px;
    background: linear-gradient(100deg, #1a1a1a 0%, #3c3c3c 50%, #2b2b2b 100%); }
  .card-photo { left: 146px; top: 0; width: 234px; height: 270px;
    background: radial-gradient(ellipse at 62% 42%, #c89c83 0%, #a98670 30%, #7d6a60 60%, #3a3a3a 100%); }
  .card .brand { left: 50px; top: 30px; font-size: 27px; }
  .card-contact { position: absolute; left: 267px; top: 186px; color: var(--white);
    font-weight: 600; font-size: 7.6px; line-height: 1.55; text-transform: uppercase; }
  .card-contact::before { content: ""; display: block; width: 13px; height: 2px; background: var(--white); margin-bottom: 4px; }
  .card-contact .web { margin-top: 9px; }
</style>
</head>
<body>
<main class="canvas">

  <section class="page features-page">
    <div class="features-band"></div>
    <div class="photo features-photo" role="img" aria-label="Porträtreihe von acht lächelnden Menschen unterschiedlicher Herkunft"></div>
    <h2 class="headline">Mit unserer Befestigungsmethode sind Sie sehr flexibel - starker Halt für jede Situation und auf Wunsch auch abnehmbar z.B. nachts beim Schlafen</h2>
    <p class="copy copy-left">Der große Vorteil unserer Befestigungsmethode liegt darin, dass Sie diese selbst umsetzen können und somit nicht jeden Monat das Studio zur Neubefestigung aufsuchen müssen. Das spart Ihnen Zeit und Geld.</p>
    <p class="copy copy-right">Wir können Ihnen Toupets und Perücken in allen Preisklassen anbieten, in verschiedenen Farben, auf Wunsch mit Grauanteil passend zum Alter des Trägers. Unsere Friseurmeisterin Frau Tiltrop berät Sie gerne, natürlich unverbindlich und kostenlos.</p>
  </section>

  <section class="page cover-page">
    <div class="photo cover-photo" role="img" aria-label="Frau mit glattem, hellbraunem Haar und Pony"></div>
    <div class="brand"><span>MOLVA Ketz</span><span class="brand-mark"></span></div>
  </section>

  <section class="page toupet-page">
    <div class="photo toupet-photo" role="img" aria-label="Lächelnder Mann mit vollem Haar in Lederjacke, sitzend mit Smartphone"></div>
    <div class="headline">
      <p>Leiden Sie an übermässigem Haarausfall?</p>
      <p>Fühlen Sie sich nicht mehr 100% wohl damit und möchten gerne wieder Ihre Attraktivität und vor allem das Wohlbefinden steigern?</p>
    </div>
    <div class="divider"><span class="divider-line"></span><span class="divider-dot"></span><span class="divider-line"></span></div>
    <p class="copy">Dann sind Sie bei uns sehr gut aufgehoben, denn wir können Ihnen Ihr Toupet individuell auf Ihre Bedürfnisse hin z.B. Farbe, Grauanteil, Größe und Styling anpassen.</p>
    <div class="brand"><span>MOLVA Ketz</span></div>
  </section>

  <section class="page wig-page">
    <div class="photo wig-photo" role="img" aria-label="Frau mit langem, rotem Haar"></div>
    <div class="wig-panel">
      <h2 class="headline">Sind Sie an einer Perücke interessiert, die augenscheinlich keinen Unterschied zu gewachsenem Haar aufweist?</h2>
      <div class="divider"><span class="divider-line"></span><span class="divider-dot"></span><span class="divider-line"></span></div>
      <p class="copy wig-copy-1">Dann sind Sie bei uns an der richtigen Adresse. Die langjährige Erfahrung im Zweithaar Bereich von Friseurmeisterin Jutta Tiltrop verspricht Ihnen optimale Beratung und ein individuell auf Sie abgestimmtes Produkt. Bei uns erhalten Sie Zugriff auf verschiedene Modelle im gesamten Preisspektrum.</p>
      <p class="copy wig-copy-2">Liegt eine von Ihrem Arzt attestierte Erkrankung vor, übernimmt Ihre Krankenkasse höchstwahrscheinlich die Kosten für Ihr Zweithaar. Die Formalitäten dazu erledigen wir gerne für Sie um Ihnen unnötigen Stress zu ersparen.</p>
    </div>
  </section>

  <section class="page card">
    <div class="photo card-photo" role="img" aria-label="Frau mit langem, glattem, hellbraunem Haar und Pony"></div>
    <div class="brand"><span>MOLVA Ketz</span><span class="brand-mark"></span></div>
    <address class="card-contact" style="font-style:normal">
      <div>MOLVA Ketz</div>
      <div>Lindhofer Str. 7</div>
      <div>44139 Velkum</div>
      <div class="web">info@molva-ketz.de</div>
      <div>molva-ketz.de</div>
    </address>
  </section>

</main>
</body>
</html>
```